Brightmere Business Card Redesign & Brightmere Update

We need to update our business cards to something more modern and fresh. Brightmere can provide the current color schemes and old design examples, but welcome creativity in helping us with this redesign. PLEASE NOTE that we no longer utilize the "tree" and/or "leaf" imagery in our branding. If able would apprecaite an update on the quality of our "words only" logo in Ai. / PNG formats too.

Target Market(s)

Investors, landowners, corporate partners, contractors

Industry/Entity Type

Environmental Restoration & Conservation

Contact Information for Business Card

Brightmere, persons name, title, mailing address, phone and email, website url

Font styles to use
Other font styles liked:
• Merriweather

Requirements
Nice to have
• Brightmere, persons name, title, mailing address, phone and email, website url, but open to ideams
Should not have
• No all back backgrounds

```html
<!DOCTYPE html>
<html lang="en">
<head>
<meta charset="utf-8">
<title>Brightmere Business Card</title>
<link rel="stylesheet" href="https://fonts.googleapis.com/css2?family=Lato:wght@300;400;700&display=swap">
<style>
  :root {
    --backdrop: #ebe7e7;
    --card: #ffffff;
    --brand-orange: #f7941d;
    --brand-blue: #1273bc;
    --ink: #111111;
    --ink-soft: #333333;
    --on-color: #ffffff;
  }
  html, body {
    margin: 0;
    width: 1200px;
    height: 1200px;
    overflow: hidden;
    background: var(--backdrop);
  }
  .sheet {
    position: relative;
    width: 1200px;
    height: 1200px;
  }
  .card {
    position: absolute;
    left: 171px;
    width: 858px;
    height: 501px;
    display: block;
  }
  .card--front { top: 78px; }
  .card--back { top: 622px; }
  .card-base { fill: var(--card); }
  .band-orange { fill: var(--brand-orange); }
  .band-blue { fill: var(--brand-blue); }
  .wordmark {
    font-family: "Lato", sans-serif;
    font-weight: 700;
    letter-spacing: -1px;
  }
  .wordmark--dark { fill: var(--ink); }
  .wordmark--light { fill: var(--on-color); }
  .person-name {
    font-family: "Lato", sans-serif;
    font-weight: 400;
    font-size: 29px;
    fill: var(--on-color);
  }
  .person-title {
    font-family: "Lato", sans-serif;
    font-weight: 300;
    font-size: 19px;
    fill: var(--on-color);
  }
  .contact-line {
    font-family: "Lato", sans-serif;
    font-weight: 300;
    font-size: 19px;
    fill: var(--on-color);
  }
  .address-line {
    font-family: "Lato", sans-serif;
    font-weight: 300;
    font-size: 19px;
    fill: var(--ink-soft);
  }
  .icon-light { fill: var(--on-color); }
  .icon-dark { fill: var(--ink-soft); }
</style>
</head>
<body>
<main class="sheet">

  <svg class="card card--front" viewBox="0 0 686 401" aria-label="Business card front">
    <rect class="card-base" width="686" height="401"/>
    <polygon class="band-orange" points="252,0 686,0 686,244"/>
    <polygon class="band-blue" points="421,105 686,254 686,401 340,401"/>
    <polygon class="band-orange" points="0,270 370,270 340,379 0,379"/>

    <text class="wordmark wordmark--dark" x="68" y="158" font-size="54">Brightmere</text>

    <text class="person-name" x="640" y="86" text-anchor="end">YOUR NAME</text>
    <text class="person-title" x="640" y="113" text-anchor="end">Owner</text>

    <g class="contact-list">
      <text class="contact-line" x="618" y="263" text-anchor="end">555-300-0000</text>
      <text class="contact-line" x="618" y="289" text-anchor="end">555-700-0000</text>
      <text class="contact-line" x="618" y="330" text-anchor="end">info@website.com</text>
      <text class="contact-line" x="618" y="356" text-anchor="end">www.website.com</text>

      <path class="icon-light" d="M632,251 l3,0 l1,3 l-1.5,1.2 a6,6 0 0 0 3.3,3.3 l1.2,-1.5 l3,1 l0,3 a1,1 0 0 1 -1,1 a10,10 0 0 1 -10,-10 a1,1 0 0 1 1,-1 z"/>
      <g class="icon-light">
        <rect x="634" y="276" width="7" height="3"/>
        <rect x="631" y="279" width="12" height="7" rx="1"/>
      </g>
      <g>
        <rect class="icon-light" x="631" y="320" width="12" height="9"/>
        <path d="M631,320 l6,5 l6,-5" fill="none" stroke="#1273bc" stroke-width="1"/>
      </g>
      <g>
        <circle class="icon-light" cx="637" cy="350" r="6"/>
        <path d="M631,350 h12 M637,344 v12" stroke="#1273bc" stroke-width="1"/>
      </g>
    </g>

    <g class="address">
      <path class="icon-dark" d="M47,288 a4,4 0 0 1 8,0 c0,3 -4,7 -4,7 c0,0 -4,-4 -4,-7 z"/>
      <rect class="icon-dark" x="45" y="296" width="12" height="1.6"/>
      <circle cx="51" cy="288" r="1.5" fill="#f7941d"/>
      <text class="address-line" x="64" y="305">100 Alder Crossing</text>
      <text class="address-line" x="64" y="331">Suit 000</text>
      <text class="address-line" x="64" y="357">Hollis, Tx 78000</text>
    </g>
  </svg>

  <svg class="card card--back" viewBox="0 0 686 401" aria-label="Business card back">
    <rect class="card-base" width="686" height="401"/>
    <rect class="band-orange" x="0" y="104" width="446" height="193"/>
    <rect class="band-blue" x="631" y="104" width="55" height="193"/>
    <text class="wordmark wordmark--light" x="425" y="220" font-size="50" text-anchor="end">Brightmere</text>
  </svg>

</main>
</body>
</html>
```